Very personalised Wedding Invitation

I want a wedding invitation very unique and personalised with the menus, ceremony time table and thank you cards. I want a mix of a nice traditional style with indian style touch. I don't want a colourful invitation, it can have max. two different colours.

The bride's name is Rosalind and the groom's name is Tarun

Reason: None of the designs submitted are what I am looking for

Target Market(s)

Invitations, personalised invitations,

Industry/Entity Type

Wedding

Logo Text

Our initials T&R To use in our wedding things

Font styles to use
Decorative
Script

Requirements
Must have
Nice to have
• I would like a chic design with a bit of indian style
Should not have

```html
<!DOCTYPE html>
<html lang="en">
<head>
<meta charset="utf-8">
<title>Rosalind &amp; Tarun — Wedding Stationery</title>
<link href="https://fonts.googleapis.com/css2?family=Roboto+Slab:wght@400;700&family=Lora:wght@400;700&family=Josefin+Slab:wght@300;400&family=Great+Vibes&display=swap" rel="stylesheet">
<style>
:root{
  --purple:#5b3d8f;
  --purple-soft:#8a72b5;
  --yellow:#f5c342;
  --yellow-pale:#fbe3a0;
  --cream:#fbf8f1;
  --paper:#f7f4ee;
  --stage:#d9d4cc;
  --sheet-bg:#585858;
  --trim:#d8403a;
  --ink-soft:#6b6170;
}
*{box-sizing:border-box;margin:0;padding:0}
html,body{width:768px;height:1200px;overflow:hidden}
body{position:relative;background:var(--stage);font-family:"Lora",serif;color:var(--purple)}

/* ---------- main invitation card ---------- */
.invite{position:absolute;left:210px;top:114px;width:330px;height:428px;background:var(--cream);box-shadow:0 2px 6px rgba(0,0,0,.25);overflow:hidden;z-index:2}
.invite .ornament{position:absolute;left:0;top:0;width:330px;height:72px}
.invite .rule-side{position:absolute;top:62px;bottom:10px;width:2px;background:var(--yellow)}
.invite .rule-side.left{left:11px}.invite .rule-side.right{right:11px}
.invite .rule-base{position:absolute;left:20px;right:20px;bottom:6px;height:2px;background:var(--yellow)}
.invite .corner{position:absolute;bottom:4px;width:8px;height:8px;background:var(--purple);border-radius:0 100% 0 100%}
.invite .corner.left{left:6px}.invite .corner.right{right:6px;transform:scaleX(-1)}
.invite .monogram{position:absolute;left:132px;top:88px;width:66px;height:66px;border-radius:50%;background:var(--yellow);display:flex;align-items:center;justify-content:center;font-family:"Great Vibes",cursive;font-size:29px;line-height:1;color:var(--purple);padding-top:3px}
.invite .hosts{position:absolute;left:0;right:0;top:174px;text-align:center;font-size:12.2px;line-height:15px;color:var(--purple)}
.invite .hosts .name{color:var(--yellow)}
.invite .hosts .script{font-family:"Great Vibes",cursive;font-size:17px;line-height:17px}
.invite .title{position:absolute;left:0;right:0;top:210px;text-align:center;font-family:"Roboto Slab",serif;font-weight:700;font-size:57px;line-height:62px;color:var(--purple);letter-spacing:-1px}
.invite .when{position:absolute;left:54px;top:304px;width:80px;text-align:center;font-family:"Roboto Slab",serif;color:var(--purple)}
.invite .when .day{font-size:10.5px;letter-spacing:2.4px;line-height:12.5px}
.invite .when .date{font-family:"Roboto Slab",serif;font-weight:400;font-size:52px;line-height:52px;color:var(--yellow);margin-top:1px;letter-spacing:-2px}
.invite .when .time{font-size:10px;letter-spacing:2.4px;line-height:12px}
.invite .when .eve{font-family:"Lora",serif;font-size:10.5px;line-height:12px}
.invite .divider{position:absolute;left:137px;top:306px;width:1.5px;height:100px;background:var(--yellow)}
.invite .venue{position:absolute;left:150px;top:304px;font-family:"Josefin Slab",serif;font-weight:400;font-size:24px;line-height:25.5px;color:var(--purple)}

/* ---------- stacked insert tabs ---------- */
.tab{position:absolute;left:210px;width:330px;background:var(--paper);box-shadow:0 2px 4px rgba(0,0,0,.22);text-align:center;font-weight:700;font-size:15px;color:var(--yellow);letter-spacing:.2px}
.tab.party{top:540px;height:72px;padding-top:28px;z-index:1}
.tab.processional{top:610px;height:66px;padding-top:26px;z-index:0}
.tab.guests{top:674px;height:70px;padding-top:30px;z-index:-1}

/* ---------- print sheet ---------- */
.sheet{position:absolute;left:0;top:860px;width:768px;height:340px;background:var(--sheet-bg)}
.crop{position:absolute;background:#8a8a8a}
.panel{position:absolute;background:var(--cream);outline:1.5px solid var(--trim)}
.panel .frame{position:absolute;inset:4px;border:1px solid #8a8590}
.panel.cover{left:4px;top:886px;width:154px;height:198px;overflow:hidden}
.panel.cover .invite{left:0;top:0;transform:scale(.4667);transform-origin:0 0;box-shadow:none}
.panel.party{left:202px;top:886px;width:155px;height:226px}
.panel.ceremony{left:395px;top:886px;width:155px;height:254px}
.panel.thanks{left:588px;top:886px;width:154px;height:288px}
.list{position:absolute;left:6px;right:6px;text-align:center;font-size:5.2px;line-height:6.4px;color:var(--ink-soft)}
.list .role{color:var(--purple);font-weight:700}
.list .role.soft{color:var(--purple-soft)}
.list .gap{height:3.4px}
.list.ceremony-steps li{list-style:none;margin-bottom:6.5px}
.list.ceremony-steps li::before{content:"\2022\00a0";color:var(--purple)}
.panel .label{position:absolute;left:0;right:0;text-align:center;font-weight:700;font-size:6.4px;color:var(--purple)}
.panel.thanks .label{color:var(--purple-soft)}
.panel.thanks .note{position:absolute;left:14px;right:14px;top:22px;text-align:center;font-size:5.4px;line-height:8.6px;color:var(--ink-soft)}
.panel.thanks .note .dateline{color:var(--purple);font-weight:700;margin-bottom:3px}
.panel.thanks .note p{margin-bottom:7px}
.panel.thanks .photo{position:absolute;left:0;right:0;top:176px;height:62px;background:var(--purple);color:#fff;font-weight:700;font-size:11px;display:flex;align-items:center;justify-content:center}
</style>
</head>
<body>

<!-- main invitation -->
<section class="invite" aria-label="Wedding invitation">
  <svg class="ornament" viewBox="0 0 330 72" role="img" aria-label="Indian paisley ornament band in purple and gold">
    <defs>
      <radialGradient id="bandTone" cx="50%" cy="0%" r="75%">
        <stop offset="0" stop-color="#5b3d8f"/>
        <stop offset=".55" stop-color="#f5c342"/>
        <stop offset="1" stop-color="#fbe3a0"/>
      </radialGradient>
    </defs>
    <path d="M0 0H330V40Q312 62 294 44Q276 66 258 48Q240 72 222 52Q204 74 186 54Q165 80 144 54Q126 74 108 52Q90 72 72 48Q54 66 36 44Q18 62 0 40Z" fill="url(#bandTone)"/>
    <circle cx="165" cy="17" r="4" fill="#fbf8f1"/>
  </svg>
  <div class="rule-side left"></div><div class="rule-side right"></div>
  <div class="rule-base"></div>
  <span class="corner left"></span><span class="corner right"></span>
  <div class="monogram">T&amp;R</div>
  <p class="hosts"><span class="name">ROSALIND P ALCANTARA</span> and <span class="name">TARUN MEHRA</span><br><span class="script">would be delighted to invite you to their</span></p>
  <h1 class="title">WEDDING</h1>
  <div class="when">
    <div class="day">Saturday<br>November</div>
    <div class="date">01</div>
    <div class="time">At 6 p.m.</div>
    <div class="eve">in the evening</div>
  </div>
  <div class="divider"></div>
  <p class="venue">The Lotus<br>Garden Hall<br>New Delhi<br>New Delhi</p>
</section>

<div class="tab party">THE WEDDING PARTY</div>
<div class="tab processional">PROCESSIONAL</div>
<div class="tab guests">TO OUR WEDDING GUESTS</div>

<!-- flat print layout -->
<section class="sheet" aria-label="Print layout">
  <span class="crop" style="left:206px;top:0;width:1px;height:20px"></span>
  <span class="crop" style="left:258px;top:0;width:1px;height:20px"></span>
  <span class="crop" style="left:398px;top:0;width:1px;height:20px"></span>
  <span class="crop" style="left:450px;top:0;width:1px;height:20px"></span>
  <span class="crop" style="left:590px;top:0;width:1px;height:20px"></span>
  <span class="crop" style="left:642px;top:0;width:1px;height:20px"></span>
</section>

<div class="panel cover">
  <section class="invite" aria-label="Invitation cover">
    <svg class="ornament" viewBox="0 0 330 72" role="img" aria-label="Indian paisley ornament band in purple and gold">
      <defs>
        <radialGradient id="bandToneSmall" cx="50%" cy="0%" r="75%">
          <stop offset="0" stop-color="#5b3d8f"/>
          <stop offset=".55" stop-color="#f5c342"/>
          <stop offset="1" stop-color="#fbe3a0"/>
        </radialGradient>
      </defs>
      <path d="M0 0H330V40Q312 62 294 44Q276 66 258 48Q240 72 222 52Q204 74 186 54Q165 80 144 54Q126 74 108 52Q90 72 72 48Q54 66 36 44Q18 62 0 40Z" fill="url(#bandToneSmall)"/>
      <circle cx="165" cy="17" r="4" fill="#fbf8f1"/>
    </svg>
    <div class="rule-side left"></div><div class="rule-side right"></div>
    <div class="rule-base"></div>
    <span class="corner left"></span><span class="corner right"></span>
    <div class="monogram">T&amp;R</div>
    <p class="hosts"><span class="name">ROSALIND P ALCANTARA</span> and <span class="name">TARUN MEHRA</span><br><span class="script">would be delighted to invite you to their</span></p>
    <h2 class="title">WEDDING</h2>
    <div class="when">
      <div class="day">Saturday<br>November</div>
      <div class="date">01</div>
      <div class="time">At 6 p.m.</div>
      <div class="eve">in the evening</div>
    </div>
    <div class="divider"></div>
    <p class="venue">The Lotus<br>Garden Hall<br>New Delhi<br>New Delhi</p>
  </section>
</div>

<div class="panel party">
  <div class="frame"></div>
  <div class="list" style="top:18px">
    <div class="role">Bride and Groom</div><div>Meera Kapoor and Daniel Ross</div><div class="gap"></div>
    <div class="role">Bride's Parents</div><div>Vikram and Asha Kapoor</div><div class="gap"></div>
    <div class="role">Groom's Parents</div><div>Peter and Lena Ross</div><div class="gap"></div>
    <div class="role soft">Bridesmaids</div><div>Nina Shah, Priya Rao, Tara Bell</div><div class="gap"></div>
    <div class="role">Groomsmen</div><div>Arjun Das, Leo Hart, Sam Iyer, Ravi Nair</div><div class="gap"></div>
    <div class="role">Grandparent of the Bride</div><div>Kamala Kapoor</div><div class="gap"></div>
    <div class="role">Grandparents of the Groom</div><div>Henry Ross, Clara Ross, June Hale</div><div class="gap"></div>
    <div class="role soft">Celebrant</div><div>Anil Verma</div>
  </div>
  <div class="label" style="top:192px">THE WEDDING PARTY</div>
</div>

<div class="panel ceremony">
  <div class="frame"></div>
  <ul class="list ceremony-steps" style="top:20px">
    <li>Greeting</li>
    <li>Ring Blessing</li>
    <li>Presentation of the Bride and Groom</li>
    <li>Reading: Anya Lind, <i>The River Between Us</i></li>
    <li>Wedding Vows</li>
    <li>Exchange of Wedding Rings</li>
    <li>Wine Box Ceremony</li>
    <li>Signing of Marriage Certificate</li>
    <li>Declaration of Support</li>
    <li>Reading: Omar Vance, <i>A Promise Kept</i></li>
    <li>Declaration of Marriage</li>
  </ul>
  <div class="label" style="top:228px">THE CEREMONY</div>
</div>

<div class="panel thanks">
  <div class="frame"></div>
  <div class="note">
    <div class="dateline">November 1, 2014</div>
    <p>Your presence here adds greatly to our joy and happiness on this special day.</p>
    <p>Today marks the beginning of our lives together. We stand before you now, declaring our love for each other and for our intent to be joined in marriage. We share with each other without reservation our lives, fortunes and future.</p>
    <p>We hope that you will continue to wish us well in our new life and we are grateful to have your love, care and best wishes for today and always!</p>
  </div>
  <div class="photo" role="img" aria-label="Photo of the couple">Your Picture</div>
  <div class="label" style="top:266px">TO OUR WEDDING GUESTS</div>
</div>

</body>
</html>
```